New Web Design Project

We need a website design for a new company called Studio Pelican. We offer :
- language tutoring for scholars or adult learners
- and other educational services associated with the French language as
*online support
*and immersive language cards games as card match, dominos, puzzle and happy family cards. Studio pelican will provide immersive and playful support to all age language learners.

Target Market(s)

Parents, French educators (teachers, tutors), Language schools, students

Industry/Entity Type

Tutoring

Coding

Coded - Design and coding required

Number of Pages Required

4 page

Requirements
Must have
• Clean and elegant design. Pages should be balanced and elements pleasingly presented
• Three buckets structure

```html
<!DOCTYPE html>
<html lang="en">
<head>
<meta charset="utf-8">
<title>Studio Pelican — Language Tutoring</title>
<link rel="stylesheet" href="https://fonts.googleapis.com/css2?family=Open+Sans:wght@400;600;700&family=Roboto+Slab:wght@400;700&display=swap">
<style>
:root{
  --plum:#a3407e;
  --plum-dark:#7e2c61;
  --gold:#d9a23f;
  --ink:#2b2b2b;
  --text:#666;
  --muted:#8a8a8a;
  --line:#e3e3e3;
  --night:#1d1d1f;
  --paper:#f3f3f3;
  --white:#fff;
}
*{box-sizing:border-box;margin:0;padding:0}
html,body{width:1200px;height:3383px;overflow:hidden}
body{font-family:"Open Sans",Arial,sans-serif;color:var(--text);background:var(--white);position:relative}
.abs{position:absolute}
section,header,footer{position:absolute;left:0;width:1200px;overflow:hidden}
h1,h2,h3{font-family:"Roboto Slab",Georgia,serif;color:var(--ink);font-weight:700}
.btn{position:absolute;display:inline-flex;align-items:center;justify-content:center;font-size:11px;letter-spacing:.5px;text-transform:uppercase;color:var(--ink);border:1px solid #bdbdbd;border-radius:3px;background:var(--white);height:26px;padding:0 12px}
p.copy{font-size:12px;line-height:19px;color:var(--text)}

/* header */
.site-header{top:0;height:117px;border-top:3px solid #bfe3ef;background:var(--white)}
.brand{position:absolute;left:101px;top:22px;display:flex;align-items:center;gap:10px}
.brand-mark{width:38px;height:38px;border-radius:50%;background:var(--gold)}
.brand-name{font-family:"Roboto Slab",Georgia,serif;font-weight:700;font-size:25px;line-height:27px;color:var(--plum)}
.phone{position:absolute;left:700px;top:26px;font-size:19px;color:var(--plum);display:flex;align-items:center;gap:8px}
.search{position:absolute;left:884px;top:25px;width:216px;height:28px;border:1px solid #d4d4d4;display:flex}
.search span{flex:1;font-size:10px;color:#999;padding:7px 8px}
.search i{width:30px;background:#e9e9e9;border-left:1px solid #d4d4d4;display:flex;align-items:center;justify-content:center}
.main-nav{position:absolute;left:492px;top:80px;display:flex;gap:0}
.main-nav a{font-size:14px;color:#555;text-decoration:none;padding:0 16px;line-height:22px}
.main-nav a.active{color:var(--plum);border-bottom:2px solid var(--plum);padding-bottom:6px}

/* hero */
.hero{top:117px;height:544px;background:linear-gradient(100deg,#3b2a22 0%,#6a5240 35%,#8b7560 55%,#4d5a66 100%)}
.hero-art{position:absolute;inset:0}
.hero-screen{position:absolute;left:720px;top:40px;width:380px;height:330px;background:linear-gradient(160deg,#dfe7ea,#3fb0d6 60%,#2b95bb);transform:skewY(-6deg);opacity:.85}
.hero-title{position:absolute;left:97px;top:212px;font-size:40px;color:var(--white);letter-spacing:1px}
.hero-lede{position:absolute;left:97px;top:268px;font-size:14px;line-height:20px;color:var(--white);font-weight:600}
.hero .btn{left:97px;top:323px;height:36px;width:119px;background:var(--plum);border:0;color:var(--white)}
.arrow{position:absolute;top:245px}

/* about */
.about{top:661px;height:478px}
.about-media{position:absolute;left:97px;top:90px;width:467px;height:296px;border:4px solid #eee;background:linear-gradient(135deg,#e9e2d6,#c9b9a6 50%,#a58d79)}
.play{position:absolute;left:50%;top:50%;transform:translate(-50%,-50%)}
.about h2{position:absolute;left:596px;top:108px;font-size:30px}
.about .rule{position:absolute;left:596px;top:155px;width:540px;height:1px;background:var(--line)}
.about .p1{position:absolute;left:596px;top:163px;width:540px}
.about .p2{position:absolute;left:596px;top:251px;width:540px}
.about .btn{left:596px;top:334px}

/* games */
.games{top:1139px;height:507px;background:linear-gradient(90deg,#9a3876 0%,#a7457f 55%,#b86a99 100%)}
.games h2{position:absolute;left:0;width:1200px;text-align:center;top:68px;font-size:28px;color:var(--white)}
.games .sub{position:absolute;left:0;width:1200px;text-align:center;top:108px;font-size:12px;color:#f1d9e8}
.hub{position:absolute;left:397px;top:304px;width:406px;height:406px;border-radius:50%;background:var(--white)}
.hub-name{position:absolute;left:0;width:1200px;top:410px;text-align:center;font-family:"Roboto Slab",Georgia,serif;font-weight:700;font-size:24px;color:var(--gold)}
.game{position:absolute;color:var(--white)}
.game b{display:block;font-family:"Roboto Slab",Georgia,serif;font-size:15px;font-weight:400}
.game small{display:block;font-size:11px;font-weight:600;color:#f3dceb}
.game.left{text-align:right}
.icon-dot{position:absolute;width:58px;height:58px;border-radius:50%;background:var(--gold);border:3px solid #ecc675;display:flex;align-items:center;justify-content:center}

/* offer */
.offer{top:1646px;height:576px}
.offer h2{position:absolute;left:0;width:1200px;text-align:center;top:84px;font-size:29px;font-weight:400}
.card{position:absolute;top:151px;width:314px}
.card .pic{height:183px}
.card h3{font-family:"Open Sans",Arial,sans-serif;font-weight:400;font-size:16px;margin-top:28px;color:var(--ink)}
.card p{margin-top:7px}
.card .btn{position:relative;margin-top:14px}

/* feedback */
.feedback{top:2222px;height:412px;background:linear-gradient(180deg,#1c1c1d,#2a2927 50%,#1a1a1a)}
.feedback h2{position:absolute;left:0;width:1200px;text-align:center;top:50px;font-size:29px;color:var(--white);font-weight:400}
.feedback .sub{position:absolute;left:0;width:1200px;text-align:center;top:107px;font-size:12px;color:#ddd}
.quote{position:absolute;top:160px;width:306px}
.quote p{font-size:12px;line-height:20px;color:#eee;padding:0 22px}
.quote .q{position:absolute;font-family:Georgia,serif;font-size:30px;color:#ddd;line-height:1}
.person{position:absolute;top:180px;display:flex;align-items:center;gap:14px}
.avatar{width:62px;height:62px;border-radius:50%;border:3px solid var(--white);background:linear-gradient(135deg,#d8c3b0,#8d7b6c)}
.person b{display:block;font-size:11px;color:var(--white)}
.person span{font-size:11px;color:#ccc}

/* news */
.news{top:2634px;height:399px}
.news h2{position:absolute;left:97px;top:77px;font-size:25px;font-weight:400}
.news .nav{position:absolute;left:1072px;top:84px;display:flex;gap:10px}
.post{position:absolute;top:147px}
.post .pic{position:absolute;left:0;top:0;width:189px;height:162px}
.post .body{position:absolute;left:214px;top:0;width:250px}
.post h3{font-family:"Open Sans",Arial,sans-serif;font-weight:400;font-size:15px;color:var(--ink)}
.post .date{display:block;margin-top:12px;font-size:12px;font-weight:700;color:var(--plum)}
.post p{margin-top:8px;font-size:11px;line-height:17px}
.post .more{display:block;margin-top:6px;font-size:12px;color:var(--ink)}

/* footer */
.site-footer{top:3033px;height:350px;background:var(--paper)}
.site-footer h4{font-family:"Open Sans",Arial,sans-serif;font-size:14px;font-weight:600;color:var(--ink);letter-spacing:.5px}
.foot-brand{position:absolute;left:97px;top:60px;display:flex;align-items:center;gap:8px}
.foot-brand .brand-mark{width:26px;height:26px}
.foot-brand .brand-name{font-size:20px;line-height:22px}
.foot-about{position:absolute;left:97px;top:130px;width:250px;font-size:11px;line-height:17px}
.socials{position:absolute;left:97px;top:212px;display:flex;gap:6px}
.socials i{width:24px;height:24px;border-radius:50%;border:1px solid #777}
.newsletter{position:absolute;left:406px;top:64px;width:250px}
.newsletter p{font-size:11px;line-height:17px;margin-top:14px}
.field{margin-top:12px;width:245px;height:38px;background:var(--white);border:1px solid #ddd;font-size:10px;color:#999;padding:12px}
.subscribe{margin-top:10px;display:inline-block;background:var(--plum);color:var(--white);font-size:11px;padding:8px 14px;text-transform:uppercase}
.contact{position:absolute;left:720px;top:64px;width:250px}
.contact ul{list-style:none;margin-top:14px}
.contact li{display:flex;gap:12px;font-size:12px;line-height:17px;margin-bottom:12px}
.links{position:absolute;left:995px;top:64px}
.links ul{list-style:none;margin-top:12px}
.links li{font-size:11px;line-height:22px}
.copyline{position:absolute;left:0;top:282px;width:1200px;height:68px;border-top:1px solid #e2e2e2;text-align:center;font-size:11px;line-height:68px;color:#777;background:var(--white)}
</style>
</head>
<body>

<header class="site-header">
  <div class="brand"><span class="brand-mark"></span><span class="brand-name">Studio<br>Pelican</span></div>
  <div class="phone">
    <svg width="18" height="18" viewBox="0 0 24 24"><path fill="#a3407e" d="M6.6 10.8a15 15 0 006.6 6.6l2.2-2.2c.3-.3.7-.4 1-.2 1.1.4 2.3.6 3.6.6.6 0 1 .4 1 1V20c0 .6-.4 1-1 1A17 17 0 013 4c0-.6.4-1 1-1h3.5c.6 0 1 .4 1 1 0 1.3.2 2.5.6 3.6.1.3 0 .7-.2 1z"/></svg>
    555-010-1290
  </div>
  <div class="search"><span>Search</span><i><svg width="11" height="11" viewBox="0 0 12 12"><circle cx="5" cy="5" r="3.6" fill="none" stroke="#555" stroke-width="1.5"/><path d="M7.6 7.6L11 11" stroke="#555" stroke-width="1.5"/></svg></i></div>
  <nav class="main-nav">
    <a class="active">Home</a><a>About Us</a><a>Our Services</a><a>Language</a><a>Testimonials</a><a>Contact Us</a>
  </nav>
</header>

<section class="hero">
  <div class="hero-art" role="img" aria-label="Photo of hands typing on a laptop whose screen shows a jigsaw puzzle, coffee cup on a wooden table">
    <div class="hero-screen"></div>
  </div>
  <h1 class="hero-title">STUDIO PELICAN</h1>
  <p class="hero-lede">Lorem ipsum dolor sit amet, consectetur adipiscing elit,<br>sed do eiusmod tempor incididunt ut labore</p>
  <span class="btn">Read More</span>
  <svg class="arrow" style="left:38px" width="26" height="50" viewBox="0 0 26 50"><path d="M22 2L4 25l18 23" fill="none" stroke="#fff" stroke-opacity=".6" stroke-width="2"/></svg>
  <svg class="arrow" style="left:1136px" width="26" height="50" viewBox="0 0 26 50"><path d="M4 2l18 23L4 48" fill="none" stroke="#fff" stroke-opacity=".6" stroke-width="2"/></svg>
</section>

<section class="about">
  <div class="about-media" role="img" aria-label="Video still of a tutor and a child learning together at a laptop">
    <svg class="play" width="60" height="60" viewBox="0 0 60 60"><circle cx="30" cy="30" r="28" fill="#2b2b2b" fill-opacity=".75"/><path d="M24 18l18 12-18 12z" fill="#fff"/></svg>
  </div>
  <h2>ABOUT STUDIO PELICAN</h2>
  <div class="rule"></div>
  <p class="copy p1">Sed ut perspiciatis unde omnis iste natus error sit voluptatem accusantium doloremque laudantium, totam rem aperiam, eaque ipsa quae ab illo inventore veritatis et quasi architecto beatae vitae dicta sunt explicabo. Nemo enim ipsam voluptatem quia voluptas sit aspernatur aut odit aut fugit, sed quia consequuntur magni dolores eos qui ratione.</p>
  <p class="copy p2">Nemo enim ipsam voluptatem quia voluptas sit aspernatur aut odit aut fugit, sed quia consequuntur magni dolores eos qui ratione voluptatem. Sed ut perspiciatis unde omnis iste natus error sit voluptatem accusantium doloremque laudantium.</p>
  <span class="btn">Read More &#9679;</span>
</section>

<section class="games">
  <h2>LANGUAGE CARDS GAMES</h2>
  <p class="sub">Starting or running a tutoring business has never been easier.</p>
  <svg class="abs" style="left:0;top:0" width="1200" height="507">
    <g stroke="#f2d9e8" stroke-width="1.5">
      <line x1="521" y1="225" x2="545" y2="312"/><line x1="390" y1="309" x2="453" y2="368"/><line x1="325" y1="424" x2="406" y2="448"/>
      <line x1="675" y1="225" x2="655" y2="312"/><line x1="801" y1="311" x2="747" y2="368"/><line x1="871" y1="426" x2="794" y2="448"/>
    </g>
    <g fill="#d9a23f"><circle cx="545" cy="312" r="4"/><circle cx="453" cy="368" r="4"/><circle cx="406" cy="448" r="4"/><circle cx="655" cy="312" r="4"/><circle cx="747" cy="368" r="4"/><circle cx="794" cy="448" r="4"/></g>
  </svg>
  <div class="hub"></div>
  <div class="hub-name">Studio Pelican</div>

  <div class="icon-dot" style="left:492px;top:196px"><svg width="26" height="26" viewBox="0 0 24 24"><path fill="#fff" d="M3 3h7v3a2 2 0 104 0V3h7v7h-3a2 2 0 100 4h3v7h-7v-3a2 2 0 10-4 0v3H3z"/></svg></div>
  <div class="icon-dot" style="left:361px;top:280px"><svg width="26" height="26" viewBox="0 0 24 24"><rect x="3" y="4" width="8" height="16" rx="1" fill="#fff"/><rect x="13" y="4" width="8" height="16" rx="1" fill="#fff"/><g fill="#d9a23f"><rect x="3" y="11.5" width="8" height="1"/><rect x="13" y="11.5" width="8" height="1"/><circle cx="7" cy="8" r="1.2"/><circle cx="17" cy="16" r="1.2"/></g></svg></div>
  <div class="icon-dot" style="left:296px;top:395px"><svg width="26" height="26" viewBox="0 0 24 24"><rect x="4" y="3" width="12" height="16" rx="1.5" fill="none" stroke="#fff" stroke-width="2"/><rect x="8" y="6" width="12" height="16" rx="1.5" fill="#fff"/></svg></div>
  <div class="icon-dot" style="left:646px;top:196px"><svg width="26" height="26" viewBox="0 0 24 24"><circle cx="12" cy="5" r="3" fill="#fff"/><path fill="#fff" d="M7 10h10v6h-3v6h-4v-6H7z"/></svg></div>
  <div class="icon-dot" style="left:772px;top:282px"><svg width="28" height="26" viewBox="0 0 26 24"><rect x="5" y="5" width="16" height="11" rx="1" fill="none" stroke="#fff" stroke-width="2"/><path d="M2 18h22v2H2z" fill="#fff"/></svg></div>
  <div class="icon-dot" style="left:842px;top:397px"><svg width="26" height="26" viewBox="0 0 24 24"><path fill="#fff" d="M22 2L2 10l7 3 2 8 4-6 5 3z"/></svg></div>

  <div class="game left" style="left:200px;width:266px;top:206px"><b>Puzzle</b><small>Nemo enim ipsam voluptatem</small></div>
  <div class="game left" style="left:100px;width:240px;top:290px"><b>Dominos</b><small>Nemo enim ipsam voluptatem</small></div>
  <div class="game left" style="left:40px;width:233px;top:406px"><b>Card Match</b><small>Nemo enim ipsam voluptatem</small></div>
  <div class="game" style="left:733px;top:188px"><b>Happy Family Cards</b><small>Nemo enim ipsam voluptatem</small></div>
  <div class="game" style="left:860px;top:274px"><b>Studio Pelican</b><small>Nemo enim ipsam voluptatem</small></div>
  <div class="game" style="left:925px;top:391px"><b>Language Learners</b><small>Nemo enim ipsam voluptatem</small></div>
</section>

<section class="offer">
  <h2>WE OFFER</h2>
  <article class="card" style="left:115px">
    <div class="pic" role="img" aria-label="Photo of a laptop on a sunlit desk" style="background:linear-gradient(135deg,#f3c27a,#c47a3c 55%,#5a3c2c)"></div>
    <h3>Language Tutoring For Scholars</h3>
    <p class="copy">Nemo enim ipsam voluptatem quia voluptas sit aspernatur aut odit aut fugit, sed quia consequuntur magni dolores eos qui ratione voluptatem sequi nesciunt.</p>
    <span class="btn">Read More</span>
  </article>
  <article class="card" style="left:458px">
    <div class="pic" role="img" aria-label="Photo of an adult learner reading a tablet in a library" style="background:linear-gradient(135deg,#b88b5c,#7e5b3b 50%,#d9c4a6)"></div>
    <h3>Adult Learners</h3>
    <p class="copy">Nemo enim ipsam voluptatem quia voluptas sit aspernatur aut odit aut fugit, sed quia consequuntur magni dolores eos qui ratione voluptatem sequi nesciunt.</p>
    <span class="btn">Read More</span>
  </article>
  <article class="card" style="left:803px">
    <div class="pic" role="img" aria-label="Photo of students working at computers in a classroom" style="background:linear-gradient(135deg,#9aa2a8,#5d6770 50%,#c7cdd1)"></div>
    <h3>Other Educational Services</h3>
    <p class="copy">Nemo enim ipsam voluptatem quia voluptas sit aspernatur aut odit aut fugit, sed quia consequuntur magni dolores eos qui ratione voluptatem sequi nesciunt.</p>
    <span class="btn">Read More</span>
  </article>
</section>

<section class="feedback">
  <h2>TUTOR FEEDBACK</h2>
  <p class="sub">Es simplemente el texto de relleno de las imprentas y archivos de texto. Lorem Ipsum ha sido el texto...</p>
  <div class="quote" style="left:100px"><span class="q" style="left:0;top:-6px">&ldquo;</span><p>Lorem Ipsum is simply dummy text of the printing and typesetting industry. Lorem Ipsum has been the industry's standard dummy text ever since the 1500s printer took...</p><span class="q" style="right:0;top:70px">&rdquo;</span></div>
  <div class="quote" style="left:447px"><span class="q" style="left:0;top:-6px">&ldquo;</span><p>Lorem Ipsum is simply dummy text of the printing and typesetting industry. Lorem Ipsum has been the industry's standard dummy text ever since the 1500s printer took...</p><span class="q" style="right:0;top:70px">&rdquo;</span></div>
  <div class="quote" style="left:792px"><span class="q" style="left:0;top:-6px">&ldquo;</span><p>Lorem Ipsum is simply dummy text of the printing and typesetting industry. Lorem Ipsum has been the industry's standard dummy text ever since the 1500s printer took...</p><span class="q" style="right:0;top:70px">&rdquo;</span></div>
  <div class="person" style="left:105px;top:289px"><div class="avatar" role="img" aria-label="Student portrait"></div><div><b>NOEL BRANDT</b><span>Student</span></div></div>
  <div class="person" style="left:457px;top:289px"><div class="avatar" role="img" aria-label="Student portrait"></div><div><b>NOEL BRANDT</b><span>Student</span></div></div>
  <div class="person" style="left:807px;top:289px"><div class="avatar" role="img" aria-label="Student portrait"></div><div><b>NOEL BRANDT</b><span>Student</span></div></div>
</section>

<section class="news">
  <h2>LATEST NEWS</h2>
  <div class="nav"><svg width="8" height="14" viewBox="0 0 8 14"><path d="M7 1L1 7l6 6" fill="none" stroke="#333" stroke-width="1.5"/></svg><svg width="8" height="14" viewBox="0 0 8 14"><path d="M1 1l6 6-6 6" fill="none" stroke="#333" stroke-width="1.5"/></svg></div>
  <article class="post" style="left:97px">
    <div class="pic" role="img" aria-label="Photo of a tutor and child at a laptop" style="background:linear-gradient(135deg,#efe4d6,#c9a98b 55%,#9c7b63)"></div>
    <div class="body">
      <h3>Nulla at diam ornare, aliquam urna</h3>
      <span class="date">APRIL 25, 2017</span>
      <p>Nulla at diam ornare, aliquam urna vel, commodo urna. Nam id risus a est luctus consectetur quis eget libero. Suspendisse potenti. Pellentesque habitant morbi tristique senectus.</p>
      <span class="more">Read More &rsaquo;</span>
    </div>
  </article>
  <article class="post" style="left:629px">
    <div class="pic" role="img" aria-label="Photo of a teacher with children at a table" style="background:linear-gradient(135deg,#c89a6e,#7a4f35 55%,#d4b69a)"></div>
    <div class="body">
      <h3>Nulla at diam ornare, aliquam urna</h3>
      <span class="date">APRIL 25, 2017</span>
      <p>Nulla at diam ornare, aliquam urna vel, commodo urna. Nam id risus a est luctus consectetur quis eget libero. Suspendisse potenti. Pellentesque habitant morbi tristique senectus.</p>
      <span class="more">Read More &rsaquo;</span>
    </div>
  </article>
</section>

<footer class="site-footer">
  <div class="foot-brand"><span class="brand-mark"></span><span class="brand-name">Studio<br>Pelican</span></div>
  <p class="foot-about">Nemo enim ipsam voluptatem quia voluptas sit aspernatur aut odit aut fugit, sed quia consequuntur magni dolores eos qui ratione voluptatem sequi nesciunt.</p>
  <div class="socials"><i></i><i></i><i></i><i></i></div>

  <div class="newsletter">
    <h4>SIGN UP FOR NEWSLETTER</h4>
    <p>Excepteur sint occaecat cupidatat non proident, sunt in culpa qui officia deserunt</p>
    <div class="field">Enter email</div>
    <span class="subscribe">Subscription</span>
  </div>

  <div class="contact">
    <h4>CONTACT US</h4>
    <ul>
      <li><svg width="12" height="16" viewBox="0 0 12 16"><path d="M6 0a6 6 0 00-6 6c0 4.5 6 10 6 10s6-5.5 6-10a6 6 0 00-6-6zm0 8.5A2.5 2.5 0 116 3.5a2.5 2.5 0 010 5z" fill="#666"/></svg><span>Studio Pelican<br>P.O. Box 120<br>Millbrook, NC 27000&nbsp; USA</span></li>
      <li><svg width="12" height="14" viewBox="0 0 24 24"><path fill="#666" d="M6.6 10.8a15 15 0 006.6 6.6l2.2-2.2c.3-.3.7-.4 1-.2 1.1.4 2.3.6 3.6.6.6 0 1 .4 1 1V20c0 .6-.4 1-1 1A17 17 0 013 4c0-.6.4-1 1-1h3.5c.6 0 1 .4 1 1 0 1.3.2 2.5.6 3.6.1.3 0 .7-.2 1z"/></svg><span>Phone:&nbsp; (555) 010.593</span></li>
      <li><svg width="13" height="12" viewBox="0 0 14 10"><rect x=".5" y=".5" width="13" height="9" fill="none" stroke="#666"/><path d="M.5.5L7 6l6.5-5.5" fill="none" stroke="#666"/></svg><span>Email: info@studiopelican.example</span></li>
    </ul>
  </div>

  <div class="links">
    <h4>QUICK LINKS</h4>
    <ul><li>Home</li><li>About us</li><li>Our Services</li><li>Language</li><li>Blog</li><li>Contact us</li></ul>
  </div>

  <div class="copyline">&copy;2016 - 2017 Studio Pelican. All Rights Reserved.</div>
</footer>

</body>
</html>
```